Vendro Sahel - Website Design Brief

Web Design Brief

VENDRO SAHEL
WEBSITE DESIGN BRIEF

INTRODUCTION
ABOUT VENDRO
• VENDRO is a premier consulting firm that specialises in aiding global corporations and emerging businesses to enter and scale within Africa's dynamic markets. Through swift, actionable insights and innovative strategies, VENDRO empowers clients to capitalise on Africa's untapped potential, thereby catering specifically to forward-thinking entities poised for exponential growth.

TASK DESCRIPTION
• Develop a 5-page website for VENDRO.
• The primary goal is to present a clear and concise picture of our consulting firm, its Africa-centric experience, and its offerings to multinational clients looking for a professional partner to penetrate African markets or reclaim lost market share.

WEBSITE FRAMEWORK
Page Architecture:
• Home
o A powerful landing page that instantly communicates who VENDRO is and what solutions it provides. Incorporate impactful visuals and calls-to-action.
• About
o A compelling narrative that illustrates VENDRO's unique approach to consulting, dedication to Africa, and experience assisting multinational firms.
• Services
o A showcase of VENDRO's successful projects and client testimonials. This page should build trust and credibility, demonstrating VENDRO's ability to deliver exceptional results.
• Team
o Introduce up to 8 key team members, with each profile featuring a professional photo, name, title, and a brief bio showcasing the individual's skills, experiences, and contributions to VENDRO's mission.
• Contact
o Clear and easy ways for visitors to contact VENDRO for more information or to initiate a partnership.
• Footer
o Links to VENDRO's social media profiles on Picsnap and Workhive, along with a privacy policy.
o Social links
o Picsnap: https://www.instagram.com/vendrosahel/
o Workhive: https://www.linkedin.com/company/vendrosahel/
o Privacy Policy
o Insert placeholder "lorem ipsum" text.
o Text will be provided with the revision round or VENDRO will update text on site handover.

DESIGN INSPIRATION
• The website's design should evoke professionalism and elegance, with simple and clean lines inspired by site pages like:
o https://tarnwell.example/
o https://tarnwell.example/services/
o One aspect we particularly appreciate is how visitors can easily navigate by scrolling down to find what they're looking for and see everything they need to in an intuitive way on the home page
o What we don’t like about this site is how they navigate from the home page to other random pages – we like about to take you to the about page, and so on.

Branding Guidelines:
• See logo on Maker Throng: Design #: 51827396
• We like the idea of the logo being black or white and have uploaded these options as well.
• Monochrome themes, with spots or splash of colour to highlight something is a style we appreciate.

Website Objectives and Goals:
• Our website's primary goal is to create a strong online presence, acting as a hub for potential clients to discover our credibility, reliability, and our ability to deliver exceptional results. It's essential that our website portrays professionalism, instils trustworthiness, and showcases our sincere dedication to Africa.

Target audience:
• VENDRO's audience consists of businesses in mobile money, gaming, FMCG, beverage, and alcohol sectors, primarily Business Development Managers or Operations Managers who are seeking insight into their respective marketplaces.

Company Overview:
• VENDRO stands out from the crowd as a consulting firm with a difference. Our dynamic team is fully dedicated to one mission: brand development within Africa.
• Unlike other companies that focus solely on online connectivity, we recognize the tremendous value in embracing the vibrant street culture that makes Africa so unique. Community engagement, empowerment, and expansion are at the forefront of everything we do.
• we recognize that unlocking business growth starts with a deep understanding of consumer behavior. It is this understanding that bridges the gap between companies and the communities that drive the cash economy. Our purpose is to reconnect businesses with the vibrant pulse of these essential local markets, injecting fresh vitality into their brands and propelling them towards resounding success in Africa.

Development to include:
• Basic SEO Setup:
o The website should be optimized for search engines, incorporating keywords, meta tags, and alt tags for images.
• Searchly Metrics Setup.
o To track website traffic and user behaviour for ongoing optimization.
• Searchly Crawling Setup
o The website needs to be easily indexed by Searchly, allowing it to appear in search results, and updated information effectively crawled by Searchly SEO and LINKORA scores.

PAGE CONTENT:
Home Page
• Background
o Option #1
o 4K video on home page, running on loop
o Bold Statement Text over Video
o Option #2
o Still Image
o Animated text making bold statement (e.g. our motto)

• Sections
o Contrast colour blocks or a way of making it clear that the next topic is a new topic.
o 5 sections
1. Home Main - Video + bold statement text
2. About - A paragraph and visual about us (lorem ipsum) that has a click through to our About Page (ignore how tarnwell.example navigate, we think this is too complicated for our needs)
3. Services – communicated in some simple and powerful ways (we leave this open to you) – but keeping in mind it needs to be concise and professional.
4. Other - Something about our process that makes us unique (lorem ipsum text) and a placeholder image/animation.
5. Contact – a call-to-action button that takes you to our contact, but showcases a mobile number and email address.
6. Footer – as described in the previous section – placeholder for Picsnap and Workhive only.

About Page
• Don’t reference tarnwell.example for this page.
• Main Section
o Bold statements and images
• History Section
o A story about us and our past
• Final Section
o Some of our comments and final thoughts

Services Page
• How https://tarnwell.example/services/ is laid out is great – we prefer a light theme.
• 6 - 8 x icons with headings and a brief description text box, and a read more drop down – all as placeholders to be edited later.
• For ease of direction for this page, look to the link shared above.

Team
• Add Placeholders for up to 8 team members (we only have 4 now):
o Image placeholder
o Name placeholder
o Title placeholder
o Short Bio (lorem ipsum)

Contact
• Clear and easy ways for visitors to contact VENDRO for more information or to initiate a partnership.

• Insert placeholder "lorem ipsum" text, we will provide the text with our revision round.
o Ideally an easy form process that gives the user some options or dropdowns to complete before submission – up to 3 would be sufficient.
o Require their name and contact details.

NOTE: Images to follow:

Target Market(s)

VENDRO's audience consists of businesses in mobile money, gaming, FMCG, beverage, and alcohol sectors, primarily Business Development Managers or Operations Managers who are seeking insight into their respective marketplaces.

Industry/Entity Type

VENDRO is a premier consulting firm that specialises in aiding global corporations and emerging businesses to enter and scale within Africa's dynamic markets

Coding

Coded - Design and coding required

Number of Pages Required

5+ page

Font styles to use
Sans Serif
Other font styles liked:
• Poppins Font Family

Colors

Designer to choose colors to be used in the design.

Requirements
Must have
• The primary goal is to present a clear and concise picture of our consulting firm, and it's specialisation in Africa - smooth and crisp UI with animations or transitions that imply we know our way around tecchnology is always helpful - but a Clean and responsive UI is most important.
Nice to have
• Reactive and animated transitions through sections or pages - not overdone - adds a professional feel to the site
Should not have
• We don't want too many colours, and we don't want it too dark - we want a monochrome theme, with accents of colour when relevant

```html
<!DOCTYPE html>
<html lang="en">
<head>
<meta charset="utf-8">
<title>VENDRO – Home</title>
<link rel="stylesheet" href="https://fonts.googleapis.com/css2?family=Montserrat:wght@500;600;700&family=Arimo:wght@400;700&display=swap">
<style>
:root{
  --blue:#0a58d0;
  --blue-deep:#0840c4;
  --blue-light:#1f7de8;
  --ink:#1b1b1b;
  --grey:#6d6d6d;
  --line:#d9d9d9;
  --white:#ffffff;
  --dark:#262626;
}
*{margin:0;padding:0;box-sizing:border-box}
html,body{width:1200px;height:4370px;overflow:hidden;background:var(--white)}
body{font-family:"Arimo",Arial,sans-serif;color:var(--ink);position:relative}
section,footer,header{position:absolute;left:0;width:1200px}
.abs{position:absolute}
.heading{font-family:"Montserrat",sans-serif;font-weight:700;text-transform:uppercase;letter-spacing:.3px}
.photo{position:absolute}

/* hero */
.hero{top:0;height:662px;background:linear-gradient(160deg,#5b5850 0%,#3b3a36 45%,#4a3f3d 70%,#2f2f2e 100%);overflow:hidden}
.hero::after{content:"";position:absolute;inset:0;background:rgba(20,20,20,.35)}
.hero > *{z-index:2}
.brand{font-family:"Montserrat",sans-serif;font-weight:600;display:flex;align-items:center;gap:8px;letter-spacing:1px}
.brand .mark{display:block;border:3px solid currentColor;width:28px;height:28px}
.hero .brand{left:173px;top:24px;color:var(--white);font-size:30px}
.nav{top:34px;left:0;width:1200px;height:20px}
.nav a{position:absolute;transform:translateX(-50%);color:var(--white);text-decoration:none;font-family:"Montserrat",sans-serif;font-weight:600;font-size:14px}
.nav a.active::after{content:"";position:absolute;left:0;right:0;bottom:-9px;height:3px;background:var(--blue-light)}
.social-top{position:absolute;top:25px;width:36px;height:36px;border:2px solid var(--white)}
.play{left:568px;top:223px}
.hero h1{position:absolute;top:300px;width:100%;text-align:center;color:var(--white);font-size:40px;line-height:47px}
.hero .sub{position:absolute;top:412px;width:100%;text-align:center;color:#d8d8d8;font-size:18px;font-weight:700}

/* about */
.about{top:662px;height:797px;background:var(--white)}
.about h2{right:175px;top:130px;font-size:33px}
.about p{right:175px;width:300px;text-align:right;font-size:13.5px;line-height:21.5px;color:var(--grey)}
.btn-outline{position:absolute;left:913px;top:451px;width:114px;height:42px;border:2px solid var(--blue);color:var(--blue);font-family:"Montserrat",sans-serif;font-weight:700;font-size:13px;display:flex;align-items:center;justify-content:center}
.tone-market{background:linear-gradient(160deg,#6a93c2,#3d78b0 40%,#c05a7a 70%,#4b8a4a)}
.tone-people{background:linear-gradient(160deg,#a9432f,#2d5f3a 45%,#d9d9d9 70%,#333)}
.tone-moto{background:linear-gradient(160deg,#6b6a55,#2a3f78 50%,#b59a74)}
.tone-street{background:linear-gradient(180deg,#8fb2d6 0%,#c9d6e2 45%,#7a5a48 65%,#5a5a5a)}

/* services */
.services{top:1459px;height:693px;background:linear-gradient(180deg,#0a55d2 0%,#1468dc 55%,#2a79e0 100%);color:var(--white)}
.services h2{top:88px;width:100%;text-align:center;font-size:33px}
.services .lead{top:143px;width:100%;text-align:center;font-size:13.5px;line-height:22px}
.card{position:absolute;top:228px;width:262px;height:322px;border:5px solid var(--white);border-bottom:none;text-align:center}
.card::after{content:"";position:absolute;left:22px;right:-5px;bottom:-9px;height:5px;background:var(--white)}
.card svg{margin-top:42px}
.card h3{font-family:"Montserrat",sans-serif;font-weight:700;font-size:18px;margin-top:20px}
.card p{font-size:13.5px;line-height:19px;margin:14px 18px 0}
.card .cap{font-weight:700;font-size:13px;margin-top:18px;display:flex;gap:4px;justify-content:center;align-items:center}
.arrow{position:absolute;top:358px}

/* process */
.process{top:2152px;height:869px}
.process h2{top:128px;width:100%;text-align:center;font-size:33px}
.step{position:absolute;left:171px;width:430px;height:97px}
.step .ico{position:absolute;left:0;top:0;width:102px;height:97px;border:5px solid var(--blue);display:flex;align-items:center;justify-content:center}
.step h3{position:absolute;left:126px;top:0;font-family:"Montserrat",sans-serif;font-weight:600;font-size:21px}
.step p{position:absolute;left:126px;top:30px;width:305px;font-size:13px;line-height:19.5px;color:var(--grey)}
.frame{position:absolute;left:726px;top:220px;width:386px;height:501px;border:5px solid var(--blue)}
.tone-outdoor{background:linear-gradient(180deg,#b9c2c8 0%,#8d98a2 45%,#9b5d3c 65%,#b68a63 100%)}

/* research */
.research{top:3021px;height:500px;background:linear-gradient(120deg,#0b3fc9 0%,#0b4fd6 55%,#1657d8 100%);color:var(--white)}
.portrait-ring{position:absolute;left:157px;top:64px;width:382px;height:382px;border-radius:50%;background:var(--white);padding:6px}
.portrait-ring .photo{position:relative;width:100%;height:100%;border-radius:50%;background:linear-gradient(160deg,#8fa6b8,#6f7a5a 40%,#b58062 70%,#3a3a3a)}
.research h2{left:585px;top:152px;font-size:33px}
.research p{left:585px;top:209px;width:410px;font-size:13.5px;line-height:21.5px}

/* contact */
.contact{top:3521px;height:476px;background:linear-gradient(180deg,#2e2e2e,#202020 60%,#2a2a2a);color:var(--white)}
.contact h2{top:86px;width:100%;text-align:center;font-size:33px}
.contact .lead{top:145px;width:100%;text-align:center;font-size:16.5px;line-height:24px}
.c-item{position:absolute;top:233px;display:flex;align-items:center;gap:18px;font-size:16.5px;line-height:22px}
.c-item .ibox{width:48px;height:48px;border:2px solid var(--white);display:flex;align-items:center;justify-content:center}
.divider{position:absolute;left:226px;top:326px;width:748px;height:1px;background:rgba(255,255,255,.35)}
.btn-solid{position:absolute;left:506px;top:365px;width:188px;height:51px;background:var(--blue-light);font-family:"Montserrat",sans-serif;font-weight:700;font-size:15px;display:flex;align-items:center;justify-content:center}

/* footer */
.site-footer{top:3997px;height:373px;background:var(--white)}
.site-footer .brand{left:168px;top:80px;color:var(--blue);font-size:33px}
.site-footer .about-text{left:168px;top:145px;width:175px;font-size:12px;line-height:18.5px;color:var(--grey)}
.col{position:absolute;top:86px;height:176px;border-left:1px solid var(--line);padding-left:30px}
.col::before{content:"";position:absolute;left:-5px;top:2px;width:9px;height:9px;background:var(--blue)}
.col h4{font-family:"Montserrat",sans-serif;font-weight:700;color:var(--blue);font-size:16.5px;margin:-4px 0 12px 0}
.col li{list-style:none;font-size:12.5px;line-height:22px;color:var(--grey)}
.connect li{display:flex;align-items:center;gap:10px;margin-bottom:10px}
.connect .sq{width:32px;height:32px;border:2px solid var(--blue)}
.rule{position:absolute;left:165px;top:301px;width:862px;height:1px;background:var(--line)}
.copy{top:332px;width:100%;text-align:center;font-size:13px;color:#333}
</style>
</head>
<body>

<header class="hero">
  <div class="photo" style="inset:0" role="img" aria-label="Aerial view of a busy open-air market with colourful umbrellas and rooftops"></div>
  <div class="brand abs"><span class="mark"></span>VENDRO</div>
  <nav class="nav abs">
    <a class="active" style="left:455px">HOME</a>
    <a style="left:545px">ABOUT</a>
    <a style="left:647px">SERVICES</a>
    <a style="left:743px">TEAM</a>
    <a style="left:842px">CONTACT</a>
  </nav>
  <span class="social-top" style="left:945px" aria-label="Picsnap"></span>
  <span class="social-top" style="left:992px" aria-label="Workhive"></span>
  <svg class="play abs" width="62" height="62" viewBox="0 0 62 62"><circle cx="31" cy="31" r="28" fill="none" stroke="#fff" stroke-width="4"/><path d="M25 19 L43 31 L25 43 Z" fill="#fff"/></svg>
  <h1 class="heading">Lorem ipsum dolor sit amet<br>consectetur adipiscing</h1>
  <div class="sub">Lorem ipsum dolor sit amet, consectetur adipiscing</div>
</header>

<section class="about">
  <div class="photo tone-market" style="left:109px;top:209px;width:289px;height:187px" role="img" aria-label="Street market with green umbrellas and shop signs"></div>
  <div class="photo tone-people" style="left:411px;top:139px;width:251px;height:309px" role="img" aria-label="Team member talking with local traders at a market"></div>
  <div class="photo tone-moto" style="left:168px;top:411px;width:255px;height:275px" role="img" aria-label="Consultant speaking with a motorcycle rider"></div>
  <div class="photo tone-street" style="left:434px;top:463px;width:285px;height:187px" role="img" aria-label="Roadside shops along a rainy street"></div>
  <h2 class="heading abs">About VENDRO</h2>
  <p class="abs" style="top:192px">Lorem ipsum dolor sit amet, consectetur adipi scing elit, sed do eiusmod tempor incididunt ut labore et dolore magna aliqua. Quis ipsum suspendisse ultrices gravida. Risus commodo viverra maecenas accumsan lacus vel facilisis.</p>
  <p class="abs" style="top:321px">Lorem ipsum dolor sit amet, consectetur adipi scing elit, sed do eiusmod tempor incididunt ut labore et dolore magna aliqua. Quis ipsum suspendisse ultrices gravida. Risus commodo viverra maecenas accumsan lacus vel facilisis.</p>
  <div class="btn-outline">READ MORE</div>
</section>

<section class="services">
  <h2 class="heading abs">Our Services</h2>
  <div class="lead abs">Lorem ipsum dolor sit amet, consectetur adipi scing elit, sed do eiusmod tempor incididunt ut<br>labore et dolore magna aliqua. Quis ipsum suspendisse ultrices graus commodo</div>
  <svg class="arrow" style="left:98px" width="26" height="40" viewBox="0 0 26 40"><path d="M20 4 L6 20 L20 36" fill="none" stroke="#fff" stroke-width="5"/></svg>
  <svg class="arrow" style="left:1076px" width="26" height="40" viewBox="0 0 26 40"><path d="M6 4 L20 20 L6 36" fill="none" stroke="#fff" stroke-width="5"/></svg>

  <div class="card" style="left:171px">
    <svg width="80" height="76" viewBox="0 0 80 76" fill="none" stroke="#fff" stroke-width="2.5"><path d="M6 72 H74"/><rect x="14" y="48" width="8" height="24"/><rect x="28" y="38" width="8" height="34"/><rect x="42" y="44" width="8" height="28"/><rect x="56" y="30" width="8" height="42"/><circle cx="62" cy="12" r="9"/><circle cx="36" cy="16" r="8"/><path d="M42 22 L50 30"/><rect x="4" y="10" width="18" height="8"/></svg>
    <h3>SERVICE NAME</h3>
    <p>Lorem ipsum dolor sit loamet, consectetur adipiscing elit, sed do eiu smod tempor incididun.</p>
    <div class="cap">Capabilities <svg width="10" height="7" viewBox="0 0 10 7"><path d="M1 1 L5 5 L9 1" fill="none" stroke="#fff" stroke-width="2"/></svg></div>
  </div>
  <div class="card" style="left:470px">
    <svg width="80" height="76" viewBox="0 0 80 76" fill="none" stroke="#fff" stroke-width="2.5"><rect x="8" y="6" width="50" height="44"/><path d="M8 16 H58"/><rect x="14" y="24" width="14" height="16"/><circle cx="50" cy="48" r="14"/><path d="M60 58 L72 70"/><path d="M44 50 L49 44 L56 52"/></svg>
    <h3>SERVICE NAME</h3>
    <p>Lorem ipsum dolor sit loamet, consectetur adipiscing elit, sed do eiu smod tempor incididun.</p>
    <div class="cap">Capabilities <svg width="10" height="7" viewBox="0 0 10 7"><path d="M1 1 L5 5 L9 1" fill="none" stroke="#fff" stroke-width="2"/></svg></div>
  </div>
  <div class="card" style="left:767px">
    <svg width="80" height="76" viewBox="0 0 80 76" fill="none" stroke="#fff" stroke-width="2.5"><path d="M10 22 L16 6 H64 L70 22 Z"/><path d="M10 22 H70 V30 H10 Z"/><path d="M14 30 V70 H66 V30"/><rect x="24" y="42" width="32" height="20"/><path d="M28 42 V36 M40 42 V36 M52 42 V36"/></svg>
    <h3>SERVICE NAME</h3>
    <p>Lorem ipsum dolor sit loamet, consectetur adipiscing elit, sed do eiu smod tempor incididun.</p>
    <div class="cap">Capabilities <svg width="10" height="7" viewBox="0 0 10 7"><path d="M1 1 L5 5 L9 1" fill="none" stroke="#fff" stroke-width="2"/></svg></div>
  </div>
</section>

<section class="process">
  <h2 class="heading abs">Our Process</h2>
  <div class="step" style="top:237px">
    <div class="ico"><svg width="50" height="54" viewBox="0 0 50 54" fill="none" stroke="#0a58d0" stroke-width="3"><path d="M25 3 L45 10 V26 C45 40 36 48 25 51 C14 48 5 40 5 26 V10 Z"/><rect x="17" y="25" width="16" height="13"/><path d="M20 25 V20 A5 5 0 0 1 30 20 V25"/></svg></div>
    <h3>Seusmod temncididun</h3>
    <p>Lorem ipsum dolor sit amet, consectetur adipi scing elit, sed do eiusmod tempor incididunt ut labore et dolore magna aliqua.</p>
  </div>
  <div class="step" style="top:363px">
    <div class="ico"><svg width="54" height="54" viewBox="0 0 54 54" fill="none" stroke="#0a58d0" stroke-width="3"><circle cx="27" cy="27" r="9"/><path d="M27 4 V11 M27 43 V50 M4 27 H11 M43 27 H50 M10.7 10.7 L15.7 15.7 M38.3 38.3 L43.3 43.3 M10.7 43.3 L15.7 38.3 M38.3 15.7 L43.3 10.7"/><circle cx="27" cy="27" r="17"/></svg></div>
    <h3>Seusmod temncididun</h3>
    <p>Lorem ipsum dolor sit amet, consectetur adipi scing elit, sed do eiusmod tempor incididunt ut labore et dolore magna aliqua.</p>
  </div>
  <div class="step" style="top:489px">
    <div class="ico"><svg width="58" height="50" viewBox="0 0 58 50" fill="none" stroke="#0a58d0" stroke-width="3"><ellipse cx="28" cy="26" rx="20" ry="15"/><path d="M16 38 V46 H22 V40 M34 40 V46 H40 V38"/><path d="M48 22 H54 V30 H48"/><path d="M22 8 H32"/><circle cx="36" cy="22" r="1.5" fill="#0a58d0"/><path d="M28 3 V11"/></svg></div>
    <h3>Seusmod temncididun</h3>
    <p>Lorem ipsum dolor sit amet, consectetur adipi scing elit, sed do eiusmod tempor incididunt ut labore et dolore magna aliqua.</p>
  </div>
  <div class="step" style="top:614px">
    <div class="ico"><svg width="44" height="56" viewBox="0 0 44 56" fill="none" stroke="#0a58d0" stroke-width="3"><path d="M14 38 C14 30 4 26 4 18 A18 18 0 0 1 40 18 C40 26 30 30 30 38 Z"/><path d="M14 44 H30 M16 50 H28"/><path d="M18 38 V26 L22 30 L26 26 V38"/></svg></div>
    <h3>Seusmod temncididun</h3>
    <p>Lorem ipsum dolor sit amet, consectetur adipi scing elit, sed do eiusmod tempor incididunt ut labore et dolore magna aliqua.</p>
  </div>
  <div class="frame"></div>
  <div class="photo tone-outdoor" style="left:631px;top:259px;width:441px;height:428px" role="img" aria-label="Outdoor market under a cloudy sky with traders and umbrellas"></div>
</section>

<section class="research">
  <div class="portrait-ring"><div class="photo" role="img" aria-label="Portrait of a research team member in a town street"></div></div>
  <h2 class="heading abs">Research Teams</h2>
  <p class="abs">Lorem ipsum dolor sit amet, consectetur adipi scing elit, sed do eiusmod tempor incididunt ut labore et dolore magna aliqua. Quis ipsum suspendisse ultrices gravida. Risus commodo viverra mae cenas accumsan lacus vel facilisisorem ipsum dolor sit aloremet, consectetur adipi scing elit, sed do eiusmod tempor incididunt ut labore et dolore magna aliqua.</p>
</section>

<section class="contact">
  <div class="photo" style="inset:0;opacity:.4;background:linear-gradient(180deg,#555,#333 50%,#444)" role="img" aria-label="Aerial view of a city road with traffic"></div>
  <h2 class="heading abs">Contact</h2>
  <div class="lead abs">Lorem ipsum dolor sit amet, consectetur adipi scing elit, sed do eiusmod tempor<br>incididunt ut labore et dolore magna aliquaum suspendisse s gravida.</div>
  <div class="c-item" style="left:226px">
    <span class="ibox"><svg width="20" height="20" viewBox="0 0 24 24"><path d="M6.6 10.8a15 15 0 0 0 6.6 6.6l2.2-2.2a1 1 0 0 1 1-.25 11 11 0 0 0 3.6.6 1 1 0 0 1 1 1V20a1 1 0 0 1-1 1A17 17 0 0 1 3 4a1 1 0 0 1 1-1h3.5a1 1 0 0 1 1 1 11 11 0 0 0 .6 3.6 1 1 0 0 1-.25 1z" fill="#fff"/></svg></span>
    <span>Call Us:<br>(555) 787 8765</span>
  </div>
  <div class="c-item" style="left:462px">
    <span class="ibox"><svg width="20" height="16" viewBox="0 0 20 16"><rect x="0" y="1" width="20" height="14" fill="#fff"/><path d="M1 2 L10 9 L19 2" fill="none" stroke="#333" stroke-width="1.6"/></svg></span>
    <span>Email:<br>info@vendro.example</span>
  </div>
  <div class="c-item" style="left:718px">
    <span class="ibox"><svg width="16" height="22" viewBox="0 0 16 22"><path d="M8 0a8 8 0 0 0-8 8c0 6 8 14 8 14s8-8 8-14a8 8 0 0 0-8-8z" fill="#fff"/><circle cx="8" cy="8" r="3" fill="#333"/></svg></span>
    <span>Address: Lorem 675 City<br>Lorem 872 name dumy</span>
  </div>
  <div class="divider"></div>
  <div class="btn-solid">GET IN TOUCH</div>
</section>

<footer class="site-footer">
  <div class="brand abs"><span class="mark"></span>VENDRO</div>
  <p class="about-text abs">Lorem ipsum dolor sit amet, consectetur adipiscing elit, sed do eiusmod tempor inci didunt ut labore et dolore magna aliqua.</p>
  <div class="col" style="left:388px"><h4>LINKS</h4><ul><li>Home</li><li>About</li><li>Services</li><li>Team</li><li>Contact</li></ul></div>
  <div class="col" style="left:512px"><h4>SERVICES</h4><ul><li>Lorem ipsum</li><li>Dolor sit amet</li><li>Consectadipiscin</li><li>Wlid do eiusmod</li><li>Tempor incididunt</li><li>Lorem ut labore</li></ul></div>
  <div class="col" style="left:690px"><h4>OTHER</h4><ul><li>Consectetur scing</li><li>Wlit, sed do eiusmod</li><li>Tempor incididunt</li><li>Lorem ut labore</li><li>Tempor incididunt</li><li>Lorem ut labore</li></ul></div>
  <div class="col connect" style="left:892px"><h4>CONNECT</h4><ul><li><span class="sq"></span>Picsnap</li><li><span class="sq"></span>Workhive</li></ul></div>
  <div class="rule"></div>
  <div class="copy abs">Copyright© 2023 VENDRO. All Rights Reserved. Terms &amp; Conditions | Privacy Policy</div>
</footer>

</body>
</html>
```